Business card design needed

I am a Flower Essence/Light Therapist and am wanting a unique card that gives information. I am looking in particular for a card that folds and I would like the company name to be embossed if possible.
The information I need help on as it has to be short and concise but give the client information on what I do. My website is www.willowtideharmony.com.au.
WHAT ARE FLOWER ESSENCES?
Flower essences are natural remedies that address negative emotional states, physical ailments, and can be taken when one wishes to develop a more positive mind-set and/or enhance one's wellbeing.

HOW DO I TAKE THEM?
Flower essences are usually ingested. They can be purchased as dilute (dosage) and concentrate (stock) strength bottles.
You can use the stock bottle itself - directions are usually written on the bottle.

Flower essences can (generally) also be used in the bath, spray bottles, added to gentle creams / oils or rubbed into the skin

Both dosage and stock strength bottles should be kept away from heat, light and radiation (e.g. computers, televisions, mobiles/cell phones).

If taken as directed, a dosage bottle course usually lasts about 2-4 weeks

HOW MUCH DO THEY COST? (inclusive of GST)
Initial Treatment (1.5hr) - $110
Includes Flower reading and personalised flower essence dosage.
Follow up visits - (30-45mins) - $75.00
Stress/Pain/Energy Management - $60.00
Meridian Healing for particular ailments - (30-45min) - $75.00
ie. anxiety, headaches, asthmas, fear etc
Light Therapy (Quevaris) - 30mins - $75.00

Reason: Still not happy with any designs

Target Market(s)

Trying to get the corporate market and everyone males and females but I think more for females and then they will talk to their husbands etc.

Industry/Entity Type

Business

Contact Information for Business Card

Willow & Tide Harmony

Requirements
Must have
• Must be folded so that people have information
Embossed
Unique not the norm
please visit www.willowtideharmony.com.au

```html
<!DOCTYPE html>
<html lang="en">
<head>
<meta charset="utf-8">
<title>Willow &amp; Tide Harmony – Folded Card</title>
<link href="https://fonts.googleapis.com/css2?family=Questrial&family=Pinyon+Script&display=swap" rel="stylesheet">
<style>
  :root {
    --stage: #000000;
    --paper: #ffffff;
    --teal: #17a89b;
    --teal-deep: #0d6f69;
    --teal-light: #5cc4bb;
    --ink: #111111;
    --text-font: "Questrial", "Century Gothic", sans-serif;
    --script-font: "Pinyon Script", cursive;
  }
  * { box-sizing: border-box; margin: 0; padding: 0; }
  html, body { width: 1200px; height: 780px; overflow: hidden; background: var(--stage); }
  body { position: relative; font-family: var(--text-font); }

  .panel { position: absolute; overflow: hidden; background: var(--paper); }
  .panel svg.panel-bg { position: absolute; inset: 0; width: 100%; height: 100%; }
  .round-all { border-radius: 12px; }
  .round-left { border-radius: 12px 0 0 12px; }

  .photo-fill { position: absolute; inset: 0;
    background: radial-gradient(ellipse at 55% 40%, var(--teal-deep) 0%, var(--teal) 45%, var(--teal-light) 100%); }

  .brand-name { position: absolute; left: 0; right: 0; text-align: center;
    font-family: var(--text-font); font-size: 22px; line-height: 1.15; color: var(--ink); }

  .contact { position: absolute; left: 0; right: 0; text-align: center; color: var(--paper);
    font-size: 16px; line-height: 1.3; }

  .price-list { position: absolute; left: 32px; top: 0; width: 258px; color: var(--paper);
    font-size: 8px; line-height: 8px; }
  .price-list li { list-style: none; position: absolute; left: 0; right: 0; }
  .price-row { display: flex; align-items: baseline; }
  .price-row .leader { flex: 1; border-bottom: 1px dotted var(--paper); margin: 0 3px; transform: translateY(-2px); }

  .cost-heading { position: absolute; right: 26px; bottom: 26px; font-family: var(--script-font);
    font-size: 19px; color: var(--ink); }
  .gst-note { position: absolute; right: 26px; bottom: 8px; font-size: 11px; font-weight: 700; color: var(--teal); }

  .essence-info { position: absolute; left: 200px; top: 20px; width: 154px; color: var(--paper); }
  .essence-info h2 { font-size: 10px; font-weight: 700; letter-spacing: .2px; margin-bottom: 2px; }
  .essence-info p { font-size: 11.4px; line-height: 1.3; }

  .web-address { position: absolute; left: 200px; bottom: 10px; font-size: 8.5px; color: var(--teal); }

  .usage-top { position: absolute; left: 14px; top: 20px; width: 160px; color: var(--paper);
    font-size: 6.4px; line-height: 8.4px; }
  .usage-top h2 { font-size: 6.6px; font-weight: 700; }
  .usage-top p { margin-bottom: 8px; }
  .usage-bottom { position: absolute; left: 14px; top: 170px; width: 160px; color: var(--teal);
    font-size: 6.4px; line-height: 8.4px; }
  .usage-bottom p { margin-bottom: 7px; }
</style>
</head>
<body>

  <!-- Top row: price list + contact panel -->
  <section class="panel round-all" style="left:412px; top:26px; width:362px; height:225px;">
    <div class="photo-fill" role="img" aria-label="Photograph of a water droplet rippling on teal water"></div>
    <svg class="panel-bg" viewBox="0 0 362 225" preserveAspectRatio="none" aria-hidden="true">
      <path d="M0,184 C120,180 250,160 362,126 L362,225 L0,225 Z" fill="var(--paper)"/>
    </svg>
    <ul class="price-list">
      <li style="top:18px;"><div class="price-row"><span>Initial Treatment (1.5hr)</span><span class="leader"></span><span>$110</span></div>
        Includes Flower reading and<br>personalised flower essence dosage.</li>
      <li style="top:58px;"><div class="price-row"><span>Follow up visits - (30-45mins)</span><span class="leader"></span><span>$75.00</span></div></li>
      <li style="top:78px;"><div class="price-row"><span>Stress/Pain/Energy Management</span><span class="leader"></span><span>$60.00</span></div></li>
      <li style="top:99px;"><div class="price-row"><span>Meridian Healing for particular ailments - (30-45min)</span><span class="leader"></span><span>$75.00</span></div>
        ie. anxiety, headaches, asthmas, fear etc</li>
      <li style="top:128px;"><div class="price-row"><span>Light Therapy (Quevaris) - 30mins</span><span class="leader"></span><span>$75.00</span></div></li>
    </ul>
    <div class="cost-heading">How Much Do They Cost?</div>
    <div class="gst-note">(Inclusive Of Gst)</div>
  </section>

  <section class="panel round-all" style="left:779px; top:26px; width:183px; height:225px;">
    <svg class="panel-bg" viewBox="0 0 183 225" preserveAspectRatio="none" aria-hidden="true">
      <path d="M0,142 C60,136 120,146 183,168 L183,225 L0,225 Z" fill="var(--teal)"/>
    </svg>
    <div class="brand-name" style="top:40px;">Willow &amp; Tide<br>Harmony</div>
    <div class="contact" style="top:156px;">Marlena Hart<br>Phone 0400 555 218</div>
  </section>

  <!-- Middle row: front of card -->
  <section class="panel round-all" style="left:412px; top:272px; width:367px; height:224px;">
    <div class="photo-fill" style="left:182px;" role="img" aria-label="Photograph of a water droplet rippling on teal water"></div>
    <svg class="panel-bg" viewBox="0 0 367 224" preserveAspectRatio="none" aria-hidden="true">
      <rect x="0" y="0" width="182" height="224" fill="var(--paper)"/>
      <path d="M0,140 C60,136 130,148 182,170 L182,224 L0,224 Z" fill="var(--teal)"/>
      <path d="M182,170 C250,196 310,192 367,176 L367,224 L182,224 Z" fill="var(--paper)"/>
    </svg>
    <div class="brand-name" style="top:38px; width:182px;">Willow &amp; Tide<br>Harmony</div>
    <div class="contact" style="top:152px; width:182px;">Marlena Hart<br>Phone 0400 555 218</div>
    <div class="essence-info">
      <h2>WHAT ARE FLOWER ESSENCES?</h2>
      <p>Flower essences are natural remedies that address negative emotional states, physical ailments, and can be taken when one wishes to develop a more positive mind-set and/or enhance one's wellbeing.</p>
    </div>
    <div class="web-address">www.willowtideharmony.com.au</div>
  </section>

  <!-- Bottom row: inside spread -->
  <section class="panel round-left" style="left:228px; top:524px; width:180px; height:225px;">
    <svg class="panel-bg" viewBox="0 0 180 225" preserveAspectRatio="none" aria-hidden="true">
      <path d="M0,186 C60,176 120,160 180,148 L180,225 L0,225 Z" fill="var(--teal)"/>
    </svg>
    <div class="brand-name" style="top:40px;">Willow &amp; Tide<br>Harmony</div>
  </section>

  <section class="panel round-all" style="left:412px; top:524px; width:367px; height:225px;">
    <div class="photo-fill" role="img" aria-label="Photograph of a water droplet rippling on teal water"></div>
    <svg class="panel-bg" viewBox="0 0 367 225" preserveAspectRatio="none" aria-hidden="true">
      <path d="M0,150 C70,140 140,150 182,170 C250,200 310,196 367,180 L367,225 L0,225 Z" fill="var(--paper)"/>
    </svg>
    <div class="usage-top">
      <h2>HOW DO I TAKE THEM?</h2>
      <p>Flower essences are usually ingested. They can be purchased as dilute (dosage) and concentrate (stock) strength bottles.<br>You can use the stock bottle itself - directions are usually written on the bottle</p>
      <p>Flower essences can (generally) also be used in the bath, spray bottles, added to gentle creams / oils or rubbed into the skin</p>
    </div>
    <div class="usage-bottom">
      <p>Both dosage and stock strength bottles should be kept away from heat, light and radiation (e.g. computers, televisions, mobiles/cell phones).</p>
      <p>If taken as directed, a dosage bottle course usually lasts about 2-4 weeks</p>
    </div>
    <div class="essence-info">
      <h2>WHAT ARE FLOWER ESSENCES?</h2>
      <p>Flower essences are natural remedies that address negative emotional states, physical ailments, and can be taken when one wishes to develop a more positive mind-set and/or enhance one's wellbeing.</p>
    </div>
    <div class="web-address">www.willowtideharmony.com.au</div>
  </section>

</body>
</html>
```